Financial advisory firm needs new business card design

Business card design , simple , elegant, professional. Will use existing logo. One side should be a solid blue background (matching blue in Logo) . info side should have basic info, maybe two color panes. one white, one a different color..maybe light grey. Please visit our website to get feel for colors and business. www.tallowmeadwealth.com

Industry/Entity Type

Financial Service

Contact Information for Business Card

Basic info..minimalist, modern, approach

Colors

Designer to choose colors to be used in the design.

Requirements
Must have
• Important regulatory requirement. The following disclosure MUST be included somewhere on the business card. It can be either front, or back, and it may be in a smaller font (but has to be legible). My interest is to satisfy the requirement with the least possible disruption to the beauty of the card design.
• All securities offered through the Harrowgate Capital, Inc. Oakhurst Lane, NJ. Member QOLTA/DWEM. Advisory services provided through HC Advisory Services, Inc. an PBR Registered Investment Advisor.

```html
<!DOCTYPE html>
<html lang="en">
<head>
<meta charset="utf-8">
<title>Tallowmead Wealth – Business Card</title>
<link href="https://fonts.googleapis.com/css2?family=Montserrat:wght@700&family=Roboto:wght@400;500&display=swap" rel="stylesheet">
<style>
  :root {
    --stage: #2b2b2d;
    --blue-deep: #0a2a8c;
    --blue-mid: #0d5fd6;
    --blue-bright: #1f9bff;
    --navy: #16417f;
    --band: #1f5fa8;
    --band-light: #3b86cf;
    --ink: #1d1d1f;
    --paper: #ffffff;
    --rule: #3a3a3a;
  }
  * { box-sizing: border-box; margin: 0; padding: 0; }
  html, body { width: 1200px; height: 904px; overflow: hidden; }
  body {
    background: var(--stage);
    position: relative;
    font-family: "Roboto", sans-serif;
  }
  .card {
    position: absolute;
    width: 600px;
    height: 343px;
    overflow: hidden;
    box-shadow: 0 14px 30px rgba(0,0,0,.45);
  }
  /* Front */
  .card-front {
    left: 70px; top: 80px;
    background: linear-gradient(125deg, var(--blue-deep) 0%, var(--blue-mid) 45%, var(--blue-bright) 70%, var(--blue-mid) 100%);
  }
  .card-front .backdrop { position: absolute; inset: 0; }
  .front-logo {
    position: absolute; left: 0; right: 0; top: 122px;
    text-align: center;
    font-family: "Montserrat", sans-serif; font-weight: 700;
    color: var(--paper); font-size: 34px; letter-spacing: 2px;
    white-space: nowrap;
  }
  .front-logo .mark {
    display: inline-block; width: 20px; height: 20px; border-radius: 50%;
    background: var(--paper); margin-right: 12px; vertical-align: 2px;
  }
  .front-web {
    position: absolute; left: 0; right: 0; bottom: 70px; text-align: center;
    color: var(--paper); font-size: 16px; letter-spacing: 1.5px;
  }
  .disclosure {
    position: absolute; left: 40px; right: 40px; bottom: 16px;
    text-align: center; color: var(--paper);
    font-size: 9.5px; line-height: 1.35; opacity: .9;
  }
  /* Back */
  .card-back { left: 530px; top: 480px; background: var(--paper); }
  .card-back .bands { position: absolute; inset: 0; }
  .back-logo {
    position: absolute; left: 40px; top: 118px; width: 220px;
    font-family: "Montserrat", sans-serif; font-weight: 700;
    color: var(--ink); font-size: 22px; letter-spacing: 1px; line-height: 1.15;
    display: flex; align-items: center; gap: 10px;
  }
  .back-logo .mark {
    flex: none; width: 14px; height: 14px; border-radius: 50%;
    background: var(--ink);
  }
  .divider {
    position: absolute; left: 282px; top: 52px; width: 1px; height: 170px;
    background: var(--rule);
  }
  .contact { position: absolute; left: 304px; top: 50px; color: var(--ink); }
  .contact .name {
    font-family: "Montserrat", sans-serif; font-weight: 700;
    color: var(--navy); font-size: 21px; line-height: 1.1;
  }
  .contact .role { font-size: 14px; margin-bottom: 8px; }
  .contact .addr { font-size: 14px; line-height: 1.3; margin-bottom: 10px; }
  .contact ul { list-style: none; font-size: 14px; }
  .contact li { display: flex; align-items: center; gap: 8px; line-height: 1.55; }
  .contact li svg { width: 13px; height: 13px; fill: var(--navy); flex: none; }
  .contact li svg.outline { fill: none; stroke: var(--navy); stroke-width: 2.4; }
  .contact .web-accent { color: var(--band); }
</style>
</head>
<body>

<section class="card card-front" aria-label="Card front">
  <div class="backdrop" role="img" aria-label="Soft abstract blue light streaks"></div>
  <div class="front-logo"><span class="mark"></span>TALLOWMEAD WEALTH</div>
  <div class="front-web">www.tallowmeadwealth.com</div>
  <p class="disclosure">All securities offered through the Harrowgate Capital, Inc. Oakhurst Lane, NJ. Member QOLTA/DWEM.<br>Advisory services provided through HC Advisory Services, Inc. an PBR Registered Investment Advisor.</p>
</section>

<section class="card card-back" aria-label="Card back">
  <svg class="bands" viewBox="0 0 600 343" preserveAspectRatio="none">
    <path d="M0,300 C180,250 380,300 600,190 L600,206 C390,312 190,268 0,318 Z" fill="var(--band-light)"/>
    <path d="M0,318 C190,268 400,320 600,214 L600,343 L0,343 Z" fill="var(--band)"/>
  </svg>
  <div class="back-logo"><span class="mark"></span><span>TALLOWMEAD<br>WEALTH</span></div>
  <div class="divider"></div>
  <div class="contact">
    <div class="name">MARCUS ELLERY</div>
    <div class="role">Manager</div>
    <div class="addr">48 Fenwick Court, Suite 110<br>Granby, NJ 07412</div>
    <ul>
      <li><svg viewBox="0 0 24 24"><path d="M6.6 10.8a15.1 15.1 0 0 0 6.6 6.6l2.2-2.2a1 1 0 0 1 1-.25 11.4 11.4 0 0 0 3.6.57 1 1 0 0 1 1 1V20a1 1 0 0 1-1 1A17 17 0 0 1 3 4a1 1 0 0 1 1-1h3.5a1 1 0 0 1 1 1c0 1.25.2 2.45.57 3.57a1 1 0 0 1-.25 1z"/></svg><span>(555) 204-6618</span></li>
      <li><svg class="outline" viewBox="0 0 24 24"><path d="M2 5h20v14H2z M2 5l10 8 10-8"/></svg><span>info@tallowmeadwealth.com</span></li>
      <li><svg viewBox="0 0 24 24"><circle cx="12" cy="12" r="10"/></svg><span>www.<span class="web-accent">tallowmeadwealth</span>.com</span></li>
    </ul>
  </div>
</section>

</body>
</html>
```